amber crest health and wellness group.

need a full website design , all information provided in word document labeled website blue print

Target Market(s)

first responders, military , people in crisis

Coding

Coded - Design and coding required

Number of Pages Required

1 page

```html
<!DOCTYPE html>
<html lang="en">
<head>
<meta charset="utf-8">
<title>Amber Crest Health &amp; Wellness Group</title>
<link href="https://fonts.googleapis.com/css2?family=DM+Sans:wght@400;500;600;700&display=swap" rel="stylesheet">
<style>
:root{
  --blue:#255b94;
  --blue-dark:#1e4f85;
  --ink:#1d1d1f;
  --text:#444a52;
  --muted:#8a9099;
  --line:#d9dde3;
  --soft:#f4f6f9;
  --white:#ffffff;
  --grey-btn:#b4b6b9;
}
*{margin:0;padding:0;box-sizing:border-box}
html,body{width:1200px;height:5043px;overflow:hidden}
body{position:relative;font-family:"DM Sans",sans-serif;color:var(--ink);background:var(--white)}
.abs{position:absolute}
.hl{color:var(--blue);font-weight:700}
.btn{position:absolute;display:flex;align-items:center;justify-content:center;border-radius:20px;font-size:13px;font-weight:500;color:var(--white);background:var(--blue);z-index:3}
.btn.light{background:var(--white);color:var(--blue-dark)}
.btn.grey{background:var(--grey-btn)}
/* top bar */
.topbar{left:0;top:0;width:1200px;height:20px;background:var(--blue-dark);color:#dfe7f1;font-size:8px;display:flex;align-items:center;padding:0 125px;z-index:3}
.topbar span{margin-right:40px;display:flex;align-items:center;gap:5px}
.topbar .social{margin-left:auto;display:flex;gap:10px}
.topbar .social i{width:7px;height:7px;border-radius:50%;background:#dfe7f1;display:block}
/* nav */
.brand{left:128px;top:34px;display:flex;align-items:center;gap:8px;font-size:17px;font-weight:700;color:var(--blue);line-height:1;z-index:3}
.brand .dot{width:22px;height:22px;border-radius:50%;background:var(--blue)}
.brand small{display:block;font-size:7px;font-weight:500;letter-spacing:.5px;margin-top:3px}
.nav{left:462px;top:42px;display:flex;gap:26px;font-size:13px;color:var(--ink);z-index:3}
.nav-cta{left:951px;top:33px;width:124px;height:34px;font-size:13px}
/* hero */
.hero-photo{left:480px;top:20px;width:720px;height:655px;background:linear-gradient(90deg,#fff 0%,rgba(236,232,228,.6) 25%,#d9d3cc 60%,#c9c3be 100%);z-index:0}
.hero-fade{left:0;top:20px;width:760px;height:655px;background:linear-gradient(90deg,#fff 55%,rgba(255,255,255,0) 100%);z-index:1}
.hero-title{left:125px;top:168px;font-size:64px;line-height:72px;font-weight:400;color:var(--ink);z-index:3}
.hero-sub{left:125px;top:400px;width:425px;font-size:18px;line-height:33px;color:#333;z-index:3}
/* who we are */
.who-photo{left:125px;top:780px;width:407px;height:470px;border-radius:40px;background:radial-gradient(circle at 50% 40%,#d7c3b2,#9fa9b4 70%,#eef0f3)}
.h2{position:absolute;font-size:42px;font-weight:400;color:var(--ink);line-height:1.1;z-index:3}
.para{position:absolute;font-size:10.5px;line-height:19px;color:var(--text)}
.checks{position:absolute;list-style:none}
.checks li{display:flex;gap:8px;font-size:12.5px;line-height:21px;color:var(--ink);margin-bottom:4px}
.checks li svg{flex:none;margin-top:5px}
/* serve cards */
.serve{position:absolute;top:1433px;width:224px;height:208px;border:1px solid #c7ccd3;border-radius:3px;background:var(--white);box-shadow:0 2px 8px rgba(0,0,0,.06);padding:18px}
.serve.active{background:var(--blue);border-color:var(--blue);color:var(--white)}
.serve .ic{width:62px;height:62px;border-radius:50%;background:var(--blue);display:flex;align-items:center;justify-content:center}
.serve.active .ic{background:var(--white)}
.serve h3{font-size:14px;font-weight:400;margin-top:18px;line-height:17px}
.serve p{font-size:9px;line-height:16px;color:var(--text);margin-top:8px}
.serve.active p{color:#e4ecf6}
/* services */
.svc-band{left:0;top:1736px;width:1200px;height:281px;background:var(--blue)}
.svc-img{position:absolute;top:1901px;width:306px;height:350px;border-radius:4px}
.svc-ic{position:absolute;top:2224px;width:56px;height:56px;border-radius:50%;background:#7a8593;border:3px solid var(--white);display:flex;align-items:center;justify-content:center}
.svc-title{position:absolute;top:2292px;width:306px;text-align:center;font-size:23px;line-height:26px;color:var(--ink)}
.svc-desc{position:absolute;top:2354px;width:306px;text-align:center;font-size:10px;line-height:20px;color:var(--text)}
/* mission */
.mission-img{left:125px;top:2476px;width:467px;height:457px;background:linear-gradient(180deg,#9ec3e6 0%,#c9dcec 55%,#8a8f93 75%,#b5b2ad 100%)}
.mission-card{left:607px;top:2476px;width:468px;height:457px;background:var(--white);border:1px solid #eceef1;box-shadow:0 4px 16px rgba(0,0,0,.07)}
/* join */
.join-photo{left:0;top:3028px;width:1200px;height:480px;background:linear-gradient(90deg,#fbf7f3 0%,#f4ebe3 40%,#e0c3a8 65%,#d2ae8f 100%)}
.join-title{left:125px;top:3118px;font-size:42px;line-height:49px;font-weight:400}
/* partners */
.partner{position:absolute;top:3702px;width:200px;height:44px;border-radius:6px;background:#dfe2e7}
/* testimonials */
.tcard{position:absolute;top:3950px;width:190px;height:270px;background:var(--white);border:1px solid #e4e6ea;padding:24px 18px;text-align:center}
.tcard.active{background:var(--blue);color:var(--white);border-color:var(--blue)}
.tcard .q{font-size:26px;line-height:14px;color:#777;text-align:left;font-weight:700}
.tcard.active .q{color:var(--white)}
.tcard p{font-size:9.5px;line-height:14px;color:var(--text);margin-top:6px}
.tcard.active p{color:#eef3f9}
.tcard .qe{text-align:right;margin-top:4px}
.tcard .who{position:absolute;left:36px;top:226px;display:flex;align-items:center;gap:10px;font-size:12px;color:#555}
.tcard.active .who{color:var(--white)}
.tcard .av{width:34px;height:34px;border-radius:50%;background:#9a8e86}
.tcard.fade{opacity:.3}
/* footer */
.footer{left:0;top:4332px;width:1200px;height:711px;background:var(--blue);color:var(--white)}
.footer .center{position:absolute;left:0;width:1200px;text-align:center}
.footer .rule{position:absolute;left:125px;width:950px;height:1px;background:rgba(255,255,255,.45)}
.fcol{position:absolute;font-size:11px;line-height:29px;text-align:center}
.fcol h4{font-size:17px;font-weight:400;margin-bottom:14px}
.ficons{position:absolute;left:545px;top:4902px;display:flex;gap:12px}
.ficons i{width:28px;height:28px;border-radius:50%;background:var(--white);display:block}
</style>
</head>
<body>

<div class="abs topbar">
  <span>+1 (555) 014-2290</span>
  <span>12 Harbour Lane, Port Ellis</span>
  <span>info@ambercrest.example</span>
  <div class="social"><i></i><i></i><i></i></div>
</div>

<div class="abs brand"><span class="dot"></span><span>AMBER CREST<small>HEALTH &amp; WELLNESS GROUP</small></span></div>
<nav class="abs nav"><span>Home</span><span>About</span><span>Services ⌄</span><span>Our Team</span><span>Join Our Team</span><span>FAQ</span></nav>
<div class="btn nav-cta">Contact Us</div>

<section>
  <div class="abs hero-photo" role="img" aria-label="Smiling clinic receptionist handing a clipboard to a client across a reception desk"></div>
  <div class="abs hero-fade"></div>
  <h1 class="abs hero-title"><span class="hl">Helping</span> Those<br>Who <span class="hl">Help</span><br>Others</h1>
  <p class="abs hero-sub">Trauma-Informed Mental Health &amp; Wellness Care For First Responders, Professionals, And The Community.</p>
  <div class="btn" style="left:125px;top:540px;width:185px;height:33px">Explore Services</div>
  <div class="btn grey" style="left:327px;top:540px;width:175px;height:33px">Meet Our Team</div>
</section>

<section>
  <div class="abs who-photo" role="img" aria-label="Group of adults stretching together in a wellness class"></div>
  <h2 class="h2" style="left:672px;top:784px"><span class="hl">Who</span> We Are</h2>
  <p class="para" style="left:672px;top:868px;width:400px">Lorem Ipsum Dolor Sit Amet Consectetur. Odio Hendrerit Mauris Et Scelerisque Ut Ipsum In. Sit Eget Non Sit Posuere Commodo Quis Pellentesque Sed. Lobortis Amet Posuere Mattis Vitae Praesent Aliquet. Mi Elit Malesuada Dui Purus.</p>
  <p class="para" style="left:672px;top:964px;width:400px">Lorem Ipsum Dolor Sit Amet Consectetur. Odio Hendrerit Mauris Et Scelerisque Ut Ipsum In. Sit Eget Non Sit Posuere Commodo Quis Pellentesque Sed.</p>
  <ul class="checks" style="left:672px;top:1036px;width:410px">
    <li><svg width="12" height="12" viewBox="0 0 12 12"><circle cx="6" cy="6" r="6" fill="#9aa0a8"/><path d="M3.3 6.2l1.8 1.8 3.6-3.8" stroke="#fff" stroke-width="1.4" fill="none"/></svg>Lorem Ipsum Dolor Sit Amet Consectetur. Nec Rhoncus Amet Felis Vel</li>
    <li><svg width="12" height="12" viewBox="0 0 12 12"><circle cx="6" cy="6" r="6" fill="#9aa0a8"/><path d="M3.3 6.2l1.8 1.8 3.6-3.8" stroke="#fff" stroke-width="1.4" fill="none"/></svg>Lorem Ipsum Dolor Sit Amet Consectetur. Egestas Integer Suspendisse Integer Sit Natoque Aliquet Proin.</li>
    <li><svg width="12" height="12" viewBox="0 0 12 12"><circle cx="6" cy="6" r="6" fill="#9aa0a8"/><path d="M3.3 6.2l1.8 1.8 3.6-3.8" stroke="#fff" stroke-width="1.4" fill="none"/></svg>Lorem Ipsum Dolor Sit Amet Consectetur. Nec Rhoncus</li>
  </ul>
  <div class="btn" style="left:672px;top:1200px;width:149px;height:35px">Learn More</div>
</section>

<section>
  <h2 class="h2" style="left:0;width:1200px;text-align:center;top:1342px"><span class="hl">Who</span> We Serve</h2>
  <div class="serve" style="left:125px">
    <div class="ic"><svg width="30" height="30" viewBox="0 0 30 30" fill="none" stroke="#fff" stroke-width="2"><path d="M15 3l10 4v7c0 7-5 11-10 13C10 25 5 21 5 14V7z"/><path d="M10 15l3.5 3.5L20 12"/></svg></div>
    <h3>First Responders (Police, Fire, EMS)</h3>
    <p>Support Designed For Those Who Serve On The Front Lines. Trauma-Informed Care For Police, Firefighters, And Paramedics.</p>
  </div>
  <div class="serve active" style="left:366px">
    <div class="ic"><svg width="30" height="30" viewBox="0 0 30 30" fill="none" stroke="#255b94" stroke-width="2"><circle cx="15" cy="15" r="11"/><path d="M15 9v12M9 15h12"/></svg></div>
    <h3>Healthcare Professionals</h3>
    <p>Compassionate Mental Health And Wellness Support For Nurses, Doctors, And Frontline Medical Workers Facing Chronic Stress.</p>
  </div>
  <div class="serve" style="left:607px">
    <div class="ic"><svg width="30" height="30" viewBox="0 0 30 30" fill="none" stroke="#fff" stroke-width="2"><rect x="6" y="5" width="11" height="21"/><rect x="17" y="12" width="8" height="14"/><path d="M9 10h5M9 15h5M9 20h5"/></svg></div>
    <h3>High-Stress Professionals</h3>
    <p>Safe, Accessible Support For Individuals And Families Seeking Emotional Healing, Wellness, And Guidance.</p>
  </div>
  <div class="serve" style="left:848px">
    <div class="ic"><svg width="30" height="30" viewBox="0 0 30 30" fill="none" stroke="#fff" stroke-width="2"><circle cx="11" cy="10" r="4"/><circle cx="20" cy="10" r="4"/><path d="M4 25c0-5 3-8 7-8s7 3 7 8M14 19c1-1 3-2 6-2 4 0 7 3 7 8"/></svg></div>
    <h3>Families &amp; Community Members</h3>
    <p>Safe, Accessible Support For Individuals And Families Seeking Emotional Healing, Wellness, And Guidance.</p>
  </div>
</section>

<section>
  <div class="abs svc-band"></div>
  <h2 class="h2" style="left:125px;top:1796px;color:#fff">Our <b>Services</b></h2>
  <div class="btn light" style="left:924px;top:1807px;width:150px;height:32px">Learn More</div>

  <div class="svc-img" style="left:125px;background:linear-gradient(160deg,#d8d2cb,#8b7565 60%,#6d7f93)" role="img" aria-label="Man with head in hands during a therapy session"></div>
  <div class="svc-img" style="left:446px;background:linear-gradient(160deg,#ece8e3,#c9b8a6 55%,#8f8a7c)" role="img" aria-label="Woman hugging a cushion while speaking with a therapist"></div>
  <div class="svc-img" style="left:767px;background:linear-gradient(160deg,#a88e72,#c2a572 45%,#d8d2c9)" role="img" aria-label="Sound therapist playing a gong beside a resting client"></div>

  <div class="svc-ic" style="left:250px"><svg width="24" height="24" viewBox="0 0 24 24" fill="none" stroke="#fff" stroke-width="1.8"><path d="M12 20S3 14 3 8.5A4.5 4.5 0 0 1 12 6a4.5 4.5 0 0 1 9 2.5C21 14 12 20 12 20z"/></svg></div>
  <div class="svc-ic" style="left:571px"><svg width="24" height="24" viewBox="0 0 24 24" fill="none" stroke="#fff" stroke-width="1.8"><circle cx="12" cy="12" r="8"/><path d="M12 7v5l3 3"/></svg></div>
  <div class="svc-ic" style="left:892px"><svg width="24" height="24" viewBox="0 0 24 24" fill="none" stroke="#fff" stroke-width="1.8"><path d="M4 12h1M7 9v6M10 6v12M13 8v8M16 5v14M19 10v4"/></svg></div>

  <div class="svc-title" style="left:125px">Mental Health<br>Therapy</div>
  <div class="svc-title" style="left:446px">Trauma &amp; First<br>Responder Support</div>
  <div class="svc-title" style="left:767px">Sound &amp; Vibration<br>Therapy</div>
  <p class="svc-desc" style="left:125px">Lorem Ipsum Dolor Sit Amet Consectetur. In Fames Orci Pulvinar Leo Massa. Blandit Sed Dolo</p>
  <p class="svc-desc" style="left:446px">Lorem Ipsum Dolor Sit Amet Consectetur. In Fames Orci Pulvinar Leo Massa. Blandit Sed Dolo</p>
  <p class="svc-desc" style="left:767px">Lorem Ipsum Dolor Sit Amet Consectetur. In Fames Orci Pulvinar Leo Massa. Blandit Sed Dolo</p>
</section>

<section>
  <div class="abs mission-img" role="img" aria-label="Group of runners jogging together outdoors under a clear sky"></div>
  <div class="abs mission-card"></div>
  <h2 class="h2" style="left:640px;top:2512px;font-size:44px"><span class="hl">Mission</span> &amp; <span class="hl">Vision</span></h2>
  <p class="para" style="left:640px;top:2608px;width:400px">Lorem Ipsum Dolor Sit Amet Consectetur. Odio Hendrerit Mauris Et Scelerisque Ut Ipsum In. Sit Eget Non Sit Posuere Commodo Quis Pellentesque Sed. Lobortis Amet Posuere Mattis Vitae Praesent Aliquet. Mi Elit Malesuada Dui Purus.</p>
  <p class="para" style="left:640px;top:2704px;width:400px">Lorem Ipsum Dolor Sit Amet Consectetur. Odio Hendrerit Mauris Et Scelerisque Ut Ipsum In. Sit Eget Non Sit Posuere Commodo Quis Pellentesque Sed.</p>
  <ul class="checks" style="left:640px;top:2774px;width:410px">
    <li><svg width="12" height="12" viewBox="0 0 12 12"><circle cx="6" cy="6" r="6" fill="#9aa0a8"/><path d="M3.3 6.2l1.8 1.8 3.6-3.8" stroke="#fff" stroke-width="1.4" fill="none"/></svg>Lorem Ipsum Dolor Sit Amet Consectetur. Nec Rhoncus Amet Felis Vel</li>
    <li><svg width="12" height="12" viewBox="0 0 12 12"><circle cx="6" cy="6" r="6" fill="#9aa0a8"/><path d="M3.3 6.2l1.8 1.8 3.6-3.8" stroke="#fff" stroke-width="1.4" fill="none"/></svg>Lorem Ipsum Dolor Sit Amet Consectetur. Egestas Integer Suspendisse Integer Sit Natoque Aliquet Proin.</li>
    <li><svg width="12" height="12" viewBox="0 0 12 12"><circle cx="6" cy="6" r="6" fill="#9aa0a8"/><path d="M3.3 6.2l1.8 1.8 3.6-3.8" stroke="#fff" stroke-width="1.4" fill="none"/></svg>Lorem Ipsum Dolor Sit Amet Consectetur. Nec Rhoncus</li>
  </ul>
</section>

<section>
  <div class="abs join-photo" role="img" aria-label="Several hands forming a heart shape together against a warm backdrop"></div>
  <h2 class="abs join-title"><span class="hl">Join</span> Our<br><span class="hl">Community</span> To<br>Support Your<br><span class="hl">Wellbeing.</span></h2>
  <div class="btn" style="left:125px;top:3373px;width:157px;height:33px">Join Us Now</div>
</section>

<section>
  <h2 class="h2" style="left:0;width:1200px;text-align:center;top:3612px">Community <span class="hl">Partners</span></h2>
  <div class="partner" style="left:0"></div>
  <div class="partner" style="left:250px"></div>
  <div class="partner" style="left:500px;background:#c5cad1"></div>
  <div class="partner" style="left:750px"></div>
  <div class="partner" style="left:1000px"></div>
</section>

<section>
  <h2 class="h2" style="left:0;width:1200px;text-align:center;top:3852px">Real <span class="hl">People.</span> Real <span class="hl">Results</span></h2>
  <div class="tcard fade" style="left:-14px"><div class="q">“</div><p>Lorem ipsum dolor sit amet consectetur. Euismod vehicula ut risus facilisis amet. Ultricies ut imperdiet amet tristique enim. Dolor donec odio turpis amet tellus. Ornare est ipsum volutpat felis sed orci mauris.</p><div class="q qe">”</div><div class="who"><span class="av"></span>— Mara Holt</div></div>
  <div class="tcard" style="left:193px"><div class="q">“</div><p>Lorem ipsum dolor sit amet consectetur. Euismod vehicula ut risus facilisis amet. Ultricies ut imperdiet amet tristique enim. Dolor donec odio turpis amet tellus. Ornare est ipsum volutpat felis sed orci mauris.</p><div class="q qe">”</div><div class="who"><span class="av"></span>— Mara Holt</div></div>
  <div class="tcard active" style="left:400px"><div class="q">“</div><p>Lorem ipsum dolor sit amet consectetur. Euismod vehicula ut risus facilisis amet. Ultricies ut imperdiet amet tristique enim. Dolor donec odio turpis amet tellus. Ornare est ipsum volutpat felis sed orci mauris.</p><div class="q qe">”</div><div class="who"><span class="av"></span>— Mara Holt</div></div>
  <div class="tcard" style="left:607px"><div class="q">“</div><p>Lorem ipsum dolor sit amet consectetur. Euismod vehicula ut risus facilisis amet. Ultricies ut imperdiet amet tristique enim. Dolor donec odio turpis amet tellus. Ornare est ipsum volutpat felis sed orci mauris.</p><div class="q qe">”</div><div class="who"><span class="av"></span>— Mara Holt</div></div>
  <div class="tcard" style="left:814px"><div class="q">“</div><p>Lorem ipsum dolor sit amet consectetur. Euismod vehicula ut risus facilisis amet. Ultricies ut imperdiet amet tristique enim. Dolor donec odio turpis amet tellus. Ornare est ipsum volutpat felis sed orci mauris.</p><div class="q qe">”</div><div class="who"><span class="av"></span>— Mara Holt</div></div>
  <div class="tcard fade" style="left:1021px"><div class="q">“</div><p>Lorem ipsum dolor sit amet consectetur. Euismod vehicula ut risus facilisis amet. Ultricies ut imperdiet amet tristique enim. Dolor donec odio turpis amet tellus. Ornare est ipsum volutpat felis sed orci mauris.</p><div class="q qe">”</div><div class="who"><span class="av"></span>— Mara Holt</div></div>
</section>

<footer class="abs footer">
  <h2 class="center" style="top:48px;font-size:40px;font-weight:400">Opening March 2026 In Port Ellis</h2>
  <p class="center" style="top:120px;font-size:17px">Be the first to connect with our clinical and wellness teams.</p>
  <div class="btn light" style="left:509px;top:178px;width:181px;height:32px;color:var(--ink)">Contact Us Now</div>
  <div class="rule" style="top:272px"></div>
  <div class="fcol" style="left:110px;top:346px;width:180px">
    <h4>Contact Us</h4>
    hello@ambercrest.example<br>
    <span style="line-height:16px;display:block;margin:6px 0 8px">Lorem ipsum dolor sit amet consectetur.</span>
    (000)-0000-000
  </div>
  <div class="center" style="top:500px;font-size:36px;font-weight:700;letter-spacing:1px;line-height:1">AMBER CREST<br><span style="font-size:11px;letter-spacing:2px;font-weight:500">HEALTH &amp; WELLNESS GROUP</span></div>
  <div class="fcol" style="left:974px;top:346px;width:120px">
    <h4>Support</h4>
    Lorem ipsum<br>Lorem<br>Lorem ipsum<br>Lorem ipsum
  </div>
  <div class="rule" style="top:650px"></div>
  <p class="center" style="top:672px;font-size:9px">© 2025 All rights reserved.</p>
</footer>
<div class="ficons" style="top:4904px"><i></i><i></i><i></i></div>

</body>
</html>
```